Need a plumber

Would like a postcard sized flyer made up. Want the design to be kept very simple.
List of services we carry out in bullet point or similar.
Phone number and email included on the flyer.
Logo to feature prominantly.

List of services: Hot water issues
Burst Pipes
Gas Plumbing
Roof leaks
Drain blockages

Target Market(s)

Mums, dads and hosehgold owners

Industry/Entity Type

Plumbing

Colors
0054AA
0677BA
7BADD7
CADEEF
E8F1F8

Requirements
Must have
• Services we off and our logo, also must say "local plumber"

```html
<!DOCTYPE html>
<html lang="en">
<head>
<meta charset="utf-8">
<title>Clearflow Plumbing Flyer</title>
<link href="https://fonts.googleapis.com/css2?family=Roboto:wght@300;400;500;700&family=Roboto+Condensed:wght@400;700&display=swap" rel="stylesheet">
<style>
  :root {
    --brand-blue: #1258a8;
    --ink: #111111;
    --paper: #ffffff;
    --backdrop: #ececec;
    --photo-deep: #3f67c4;
    --photo-mid: #7ba3dc;
    --photo-light: #e8f1f8;
  }
  * { margin: 0; padding: 0; box-sizing: border-box; }
  html, body { width: 1200px; height: 1200px; overflow: hidden; }
  body {
    background: var(--backdrop);
    font-family: "Roboto", Arial, sans-serif;
    position: relative;
  }
  .flyer {
    position: absolute;
    left: 233px; top: 60px;
    width: 734px; height: 1080px;
    background: var(--paper);
    overflow: hidden;
  }
  .header {
    position: absolute; left: 0; top: 0;
    width: 100%; height: 260px;
    background: var(--brand-blue);
  }
  .header-rule {
    position: absolute; left: 0; top: 262px;
    width: 100%; height: 9px;
    background: var(--ink);
  }
  .brand-badge {
    position: absolute; left: 55px; top: 48px;
    width: 188px; height: 188px;
    border-radius: 50%;
    background: var(--ink);
    border: 3px solid var(--paper);
    display: flex; flex-direction: column;
    align-items: center; justify-content: center;
    color: var(--paper);
    font-weight: 700;
    font-size: 22px;
    letter-spacing: 3px;
    line-height: 1.3;
    text-align: center;
  }
  .headline {
    position: absolute; left: 290px; top: 50px;
    width: 410px;
    color: var(--paper);
    line-height: 1;
    font-family: "Roboto Condensed", "Arial Narrow", sans-serif;
    white-space: nowrap;
  }
  .headline-top {
    display: block;
    font-weight: 400;
    font-size: 79px;
  }
  .headline-main {
    display: block;
    font-weight: 700;
    font-size: 88px;
    margin-top: 14px;
  }
  .pill {
    position: absolute; left: 202px;
    width: 333px; height: 43px;
    border-radius: 22px;
    background: var(--brand-blue);
    color: var(--paper);
    font-family: "Roboto Condensed", "Arial Narrow", sans-serif;
    font-weight: 700;
    font-size: 38px;
    line-height: 43px;
    text-align: center;
  }
  .pill-services { top: 288px; }
  .pill-contact { top: 446px; }
  .services { list-style: none; }
  .service {
    position: absolute;
    font-size: 23px;
    color: var(--ink);
    padding-left: 26px;
    line-height: 1;
    white-space: nowrap;
  }
  .service::before {
    content: "";
    position: absolute; left: 0; top: 7px;
    width: 12px; height: 12px; border-radius: 50%;
    background: var(--brand-blue);
  }
  .contact-item {
    position: absolute; top: 510px;
    display: flex; align-items: center; gap: 14px;
    font-size: 23px; color: var(--ink);
    white-space: nowrap;
  }
  .contact-phone { left: 53px; }
  .contact-email { left: 400px; }
  .contact-icon { width: 34px; height: 34px; }
  .photo-arch {
    position: absolute; left: 0; top: 540px;
    width: 734px; height: 540px;
  }
</style>
</head>
<body>
  <main class="flyer">
    <header class="header">
      <div class="brand-badge">CLEARFLOW<br>PLUMBING</div>
      <h1 class="headline">
        <span class="headline-top">NEED LOCAL</span>
        <span class="headline-main">PLUMBER?</span>
      </h1>
    </header>
    <div class="header-rule"></div>

    <h2 class="pill pill-services">Get Our Services:</h2>
    <ul class="services">
      <li class="service" style="left:52px;top:353px;">Hot water issues</li>
      <li class="service" style="left:314px;top:353px;">Burst pipes</li>
      <li class="service" style="left:515px;top:353px;">Gas plumbing</li>
      <li class="service" style="left:182px;top:392px;">Roof leaks</li>
      <li class="service" style="left:381px;top:392px;">Drain blockages</li>
    </ul>

    <h2 class="pill pill-contact">Contact Us:</h2>
    <div class="contact-item contact-phone">
      <svg class="contact-icon" viewBox="0 0 34 34" aria-hidden="true">
        <circle cx="17" cy="17" r="16" fill="#111"/>
        <circle cx="17" cy="17" r="12" fill="#fff"/>
        <path d="M11 10 l3 -1 l2 4 l-2 2 q1 3 4 4 l2 -2 l4 2 l-1 3 q-9 1 -12 -12z" fill="#111"/>
      </svg>
      <span>123 123 123</span>
    </div>
    <div class="contact-item contact-email">
      <svg class="contact-icon" viewBox="0 0 34 34" aria-hidden="true">
        <circle cx="17" cy="17" r="16" fill="#111"/>
        <circle cx="17" cy="17" r="12" fill="#fff"/>
        <rect x="10" y="12" width="14" height="10" fill="none" stroke="#111" stroke-width="1.8"/>
        <path d="M10 12 L17 18 L24 12 M10 22 L15 17 M24 22 L19 17" fill="none" stroke="#111" stroke-width="1.5"/>
      </svg>
      <span>yourname@email.com</span>
    </div>

    <svg class="photo-arch" viewBox="0 0 734 540">
      <defs>
        <linearGradient id="photoTone" x1="0" y1="0" x2="1" y2="1">
          <stop offset="0" stop-color="#e8f1f8"/>
          <stop offset="0.5" stop-color="#7ba3dc"/>
          <stop offset="1" stop-color="#3f67c4"/>
        </linearGradient>
        <clipPath id="archClip"><circle cx="367" cy="430" r="396"/></clipPath>
      </defs>
      <circle cx="367" cy="430" r="408" fill="none" stroke="#111" stroke-width="11"/>
      <rect x="0" y="0" width="734" height="540" fill="url(#photoTone)" clip-path="url(#archClip)"
            role="img" aria-label="Photo of a plumber in a blue cap and shirt fixing pipes under a sink, with wrenches on the floor"/>
    </svg>
  </main>
</body>
</html>
```